DEAN COLLOPY PROPERTY SERVICES

I want a business card that is clean and simple.
'Dean Collopy Property Services' is the title.
Somewhere on the card needs to be 'Carpentry, Tiling, painting and garden services'

On the back of card
PH 087 394 1526
email: deancollopypropertyservices@fernmail.net

I have attached a picture of my other business. I would like the font and design to be similar to the bathroom business.

Many thanks.

```html
<!DOCTYPE html>
<html lang="en">
<head>
<meta charset="utf-8">
<title>Dean Collopy Property Services – Business Card Back</title>
<link rel="stylesheet" href="https://fonts.googleapis.com/css2?family=Roboto:wght@300;400&display=swap">
<style>
  :root {
    --navy: #383d66;
    --navy-deep: #2f3459;
    --navy-light: #474c78;
    --edge: #ffffff;
    --ink: #f2f3f8;
  }
  html, body {
    margin: 0;
    padding: 0;
    width: 1200px;
    height: 705px;
    overflow: hidden;
    background: var(--edge);
  }
  .card-back {
    position: relative;
    width: 1200px;
    height: 705px;
    background: var(--navy);
    overflow: hidden;
  }
  .scene-backdrop {
    position: absolute;
    inset: 0;
    background:
      radial-gradient(ellipse 420px 160px at 580px 510px, rgba(90, 96, 140, 0.55), transparent 70%),
      linear-gradient(90deg, var(--navy) 0%, var(--navy) 22%, var(--navy-deep) 22%, var(--navy-deep) 39%, var(--navy) 39%, var(--navy) 100%),
      var(--navy);
  }
  .scene-backdrop::after {
    content: "";
    position: absolute;
    left: 0; right: 0; bottom: 0;
    height: 140px;
    background: linear-gradient(180deg, transparent, rgba(40, 45, 80, 0.6));
  }
  .trim-edges {
    position: absolute;
    inset: 0;
    width: 1200px;
    height: 705px;
  }
  .trim-edges polygon { fill: var(--edge); }
  .contact {
    position: absolute;
    left: 0;
    right: 0;
    top: 300px;
    text-align: center;
    color: var(--ink);
    font-family: "Roboto", Arial, sans-serif;
  }
  .contact-phone {
    margin: 0;
    font-size: 38px;
    font-weight: 400;
    letter-spacing: 1.5px;
    line-height: 1;
  }
  .contact-email {
    margin: 14px 0 0;
    font-size: 35px;
    font-weight: 300;
    letter-spacing: 0.2px;
    line-height: 1;
  }
</style>
</head>
<body>
  <div class="card-back">
    <div class="scene-backdrop" role="img" aria-label="Navy-tinted bathroom scene with freestanding bath, pendant lights, tiled wall and potted plants"></div>
    <svg class="trim-edges" viewBox="0 0 1200 705" aria-hidden="true">
      <polygon points="0,24 31,48 31,640 0,664"/>
      <polygon points="1200,24 1169,48 1169,640 1200,664"/>
    </svg>
    <div class="contact">
      <p class="contact-phone">PH 087 394 1526</p>
      <p class="contact-email">email: deancollopypropertyservices@fernmail.net</p>
    </div>
  </div>
</body>
</html>
```